Medical Learning Web Design Project

The web site will be a site for medical students. It is aimed at providing a collaborative place for students to study, learn, question each other and challenge each other with learning. The site needs to have a section on the page that is for the content and this needs to be relatively clean and clinical. The surrounding elements will be informative (for the statistics, challenge etc). There will also be a slide-out screen that allows for the social/friend elements of the site.

The colour scheme needs to be clean and clinical where appropriate, but also engaging and exciting for the social/competitive elements.
Updates

Just for clarity: The site isn't expected to be 'coded' ... it is just the layered PSD files that I need.

Also, with regards to the navigation buttons ... they will never ALL be present at the same time so don't feel the need to design all on one page, but creativity around allowing few or many on a page will be an advantage ...

Thanks

Hi,

Please note that the image uploaded has been done as a wireframe by the developers. I am looking for a more creative and engaging way of presenting that content ...

Thanks

Hi all

Thank you all for the designs so far ...!

Please have a look at the new uploaded file, I am also looking not just for a 'templated home page' but also some different layouts that are represented in these wireframes. If the various layouts represented can be condensed down into 1 or 2 page templates with appropriate colour schemes to capture the type of content on the page (as already mentioned ... social .. competitive ... learning), then that will help me live the concepts better too! The friends tab for instance I have envisaged as a slider covering the screen and then sliding back when complete ... but let me see what creativity you can give to this ...!

Many thanks

Target Market(s)

Medical Students

Industry/Entity Type

Medical

Requirements
Must have
• - Not cluttered appearance
- Dynamic navigation (ie. site will be developed to only show relevant navigation buttons on each page ...)
- Navigation buttons (need to be individual buttons) will be: 'Home', 'Take the tour', 'What your peers say', 'Subscriptions', 'Free Signup', 'Contact us', 'Moderation', 'Statistics', 'Competition', 'Answer Questions', 'Post Questions', 'My profile', 'Friends'
- Please also ensure it is engaging for social elements and competitive elements (perhaps slightly different design for pages focussed on each element)
- Please also ensure that there is a masculine design and feminine design that has continuity for the site but depending on gender the design can be tailored to be more appealing (that means perhaps male social design, male competitive design, female social design, female competitive design ... without loosing continuity through the site).
- Photoshop PSD format
- Pixel perfect at least 1000 pixels wide (but the design needs to allow for various monitor sizes (only desktop or laptops ... not tablets or smart phones)

```html
<!DOCTYPE html>
<html lang="en">
<head>
<meta charset="utf-8">
<title>Medora - The Medical Peer Review</title>
<link rel="stylesheet" href="https://fonts.googleapis.com/css2?family=Source+Sans+3:wght@400;600;700&display=swap">
<style>
:root{
  --blue:#0a7cc4;
  --blue-dark:#0e5f97;
  --hero-1:#0d4f80;
  --hero-2:#0a3658;
  --ink:#222;
  --muted:#555;
  --line:#d6d6d6;
  --panel-bg:#fff;
  --page-bg:#f3f3f3;
  --feed:#4a88c2;
  --social-head:#e3e8f3;
  --footer-1:#3a3a3a;
  --footer-2:#050505;
}
*{box-sizing:border-box;margin:0;padding:0}
html,body{width:1200px;height:978px;overflow:hidden}
body{position:relative;background:linear-gradient(#f1f1f1,#fff 420px,#fff);font-family:"Source Sans 3",Arial,sans-serif;color:var(--ink)}
.abs{position:absolute}
.header{left:0;top:0;width:1200px;height:145px;background:linear-gradient(#fff,#f4f4f4 70%,#e9e9e9)}
.header-rule{left:0;top:145px;width:1200px;height:8px;background:linear-gradient(var(--blue),var(--blue-dark))}
.brand{left:120px;top:22px;font-size:40px;font-weight:700;color:var(--blue);letter-spacing:-.5px;line-height:1}
.tagline{left:117px;top:64px;font-size:13px;font-weight:600;color:#444}
.quote{left:300px;top:11px;width:418px;text-align:right;font-size:12.5px;line-height:16px;color:#222}
.web-label{left:754px;top:12px;font-size:13px;font-weight:700;color:#333}
.web-icons{left:887px;top:9px;display:flex;gap:3px}
.web-icons span{width:18px;height:18px;border-radius:3px;display:block}
.field-label{font-size:14px;font-weight:600;color:#333}
.field{width:134px;height:28px;background:#fff;border:1px solid #cfcfcf;border-radius:3px;box-shadow:inset 0 1px 2px rgba(0,0,0,.08)}
.login{left:1026px;top:62px;width:57px;height:27px;border-radius:3px;background:linear-gradient(#2a9ae0,#0a6db0);color:#fff;font-size:14px;font-weight:700;text-align:center;line-height:27px}
.tab{top:112px;height:33px;border:1px solid #cfcfcf;border-bottom:none;border-radius:5px 5px 0 0;background:linear-gradient(#fff,#e6e6e6);font-size:14px;font-weight:700;color:#111;text-align:center;line-height:34px}
.tab.active{top:110px;height:35px;background:linear-gradient(#2c9be0,#0a72b8);border-color:#0a72b8;color:#fff;line-height:38px}
.news{left:110px;top:160px;width:605px;height:30px;border-radius:3px;background:linear-gradient(#4a4a4a,#1a1a1a);color:#fff;font-size:15px;padding-left:12px;line-height:31px;letter-spacing:.3px}
.chip{height:18px;border:1px solid #b9c4d6;border-radius:2px;background:linear-gradient(#fff,#e4e9f1);font-size:11px;color:#3b5a95;line-height:16px;padding:0 4px}
.count{height:16px;border:1px solid #ccc;background:#fff;font-size:11px;color:#333;line-height:14px;padding:0 3px}
.hero{left:111px;top:199px;width:979px;height:339px;background:radial-gradient(ellipse at 30% 40%,var(--hero-1),var(--hero-2) 80%)}
.hero-title{left:143px;top:231px;font-size:27px;font-weight:700;color:#fff}
.hero-list{left:149px;top:283px;list-style:none;color:#fff;font-size:15px;font-weight:600}
.hero-list li{height:30px;line-height:24px;display:flex;gap:8px;align-items:center}
.photo{width:212px;height:147px;background:#fff;padding:7px;box-shadow:0 2px 6px rgba(0,0,0,.4)}
.photo div{width:100%;height:100%}
.arrow{width:37px;height:38px;background:#111;border-radius:4px;display:flex;align-items:center;justify-content:center}
.panel{top:584px;height:273px;background:var(--panel-bg);border:1px solid var(--line);border-radius:3px}
.panel-head{height:36px;background:linear-gradient(#fff,#e8e8e8);border-bottom:1px solid var(--line);font-size:18px;font-weight:600;color:#333;padding-left:13px;line-height:36px}
.video{left:121px;top:623px;width:351px;height:225px}
.video-frame{width:351px;height:205px;background:linear-gradient(135deg,#b9703a,#7a6a5c 45%,#3d3a40)}
.video-bar{width:351px;height:20px;background:linear-gradient(#f2f2f2,#cdcdcd);display:flex;align-items:center;font-size:10px;color:#333;gap:8px;padding:0 6px}
.feed{left:496px;top:588px;width:287px;height:261px;background:var(--feed);border-radius:5px}
.feed-body{left:4px;top:52px;width:279px;height:172px;background:#fff;border-radius:4px}
.tw{padding:5px 4px 4px;border-bottom:1px solid #e5e5e5;font-size:12.5px;line-height:14px;color:#111}
.tw a{color:#2a6aa8;text-decoration:none}
.tw .who{color:#2a6aa8}
.tw .meta{font-size:9.5px;color:#2a6aa8;margin-top:1px}
.social{left:797px;top:584px;width:294px;height:273px;border:1px solid #c7cfe0;border-radius:3px;background:#fff}
.social-head{height:62px;background:var(--social-head);border-bottom:1px solid #c7cfe0}
.friend{width:50px;text-align:center;font-size:10px;color:#555}
.friend div{width:50px;height:50px;margin-bottom:5px}
.footer{left:0;top:900px;width:1200px;height:78px;background:linear-gradient(var(--footer-1),var(--footer-2))}
.footer-nav{top:916px;left:0;width:1200px;text-align:center;color:#fff;font-size:13px;font-weight:600;word-spacing:2px}
.footer-nav span{margin:0 13px}
.copy{top:940px;left:0;width:1200px;text-align:center;color:#fff;font-size:13px;font-weight:600}
</style>
</head>
<body>
<header>
  <div class="abs header"></div>
  <div class="abs header-rule"></div>
  <div class="abs brand">Medora</div>
  <div class="abs tagline">The Medical Peer Review</div>
  <p class="abs quote">Medora keeps me ahead of the game constantly testing my knowledge..."<br>-- Sam,doctor in training, University of Northfield</p>
  <div class="abs web-label">Medora on the web:</div>
  <div class="abs web-icons">
    <span style="background:#3b5998"></span><span style="background:#5bbfe9"></span><span style="background:#1f6fa8"></span><span style="background:#5a7db8"></span><span style="background:#d8d8e8"></span><span style="background:#3aa43a"></span><span style="background:#4aa0e6"></span><span style="background:#2f4fa0"></span><span style="background:#f08a1c"></span>
  </div>
  <div class="abs field-label" style="left:739px;top:45px">Username</div>
  <div class="abs field" style="left:735px;top:63px"></div>
  <div class="abs field-label" style="left:885px;top:46px">Password</div>
  <div class="abs field" style="left:882px;top:63px"></div>
  <div class="abs login">Login</div>
  <nav>
    <div class="abs tab active" style="left:339px;width:81px">Home</div>
    <div class="abs tab" style="left:426px;width:106px">Take The Tour</div>
    <div class="abs tab" style="left:541px;width:146px">What YourPeers Say</div>
    <div class="abs tab" style="left:694px;width:135px">Subsription Plans</div>
    <div class="abs tab" style="left:836px;width:100px">Free Signup</div>
    <div class="abs tab" style="left:943px;width:128px">Contact Us</div>
  </nav>
</header>

<div class="abs news">about 2 days ago: Medora is now on social. Follow us here.</div>
<div class="abs chip" style="left:755px;top:167px">&#9632; Like</div>
<div class="abs count" style="left:806px;top:168px">84</div>
<div class="abs chip" style="left:855px;top:169px;height:14px;line-height:12px;font-size:9px">+1</div>
<div class="abs count" style="left:882px;top:169px;height:14px;line-height:12px">2</div>
<div class="abs chip" style="left:926px;top:164px;color:#2a6aa8;background:linear-gradient(#fff,#d9ecf9);border-color:#9cc6e4">&#9679; Share</div>
<div class="abs count" style="left:984px;top:164px;width:36px;height:18px;text-align:center;line-height:16px;color:#2a6aa8">11</div>

<section>
  <div class="abs hero"></div>
  <h1 class="abs hero-title">Medora - The Medical Peer Review</h1>
  <ul class="abs hero-list">
    <li>&#10148; <span>Test your medical knownledge</span></li>
    <li>&#10148; <span>Answer a vast array of medical question</span></li>
    <li>&#10148; <span>Earn trophies as your knowledge inscreases</span></li>
    <li>&#10148; <span>Rate question from peers</span></li>
    <li>&#10148; <span>Ask your own question</span></li>
    <li>&#10148; <span>Link to your friends and check their progress</span></li>
    <li>&#10148; <span>29.903 Questions answered!</span></li>
  </ul>
  <div class="abs photo" style="left:574px;top:217px"><div role="img" aria-label="Medical students in white coats reviewing notes in a hospital corridor" style="background:linear-gradient(135deg,#cdb79a,#e9e4dc 50%,#8a7868)"></div></div>
  <div class="abs photo" style="left:811px;top:218px"><div role="img" aria-label="Group of smiling young doctors in white coats" style="background:linear-gradient(135deg,#c8ccd2,#eceae6 55%,#b49378)"></div></div>
  <div class="abs photo" style="left:574px;top:378px"><div role="img" aria-label="Students in white coats gathered in a hospital ward" style="background:linear-gradient(135deg,#9a7a52,#d9d3c9 50%,#6e5a44)"></div></div>
  <div class="abs photo" style="left:811px;top:378px"><div role="img" aria-label="Student practising a clinical examination with classmates" style="background:linear-gradient(135deg,#cdb8a6,#e8e6e4 45%,#6fb7bf)"></div></div>
  <div class="abs arrow" style="left:104px;top:335px"><svg width="14" height="20" viewBox="0 0 14 20"><path d="M11 2 3 10l8 8" fill="none" stroke="#fff" stroke-width="3.5"/></svg></div>
  <div class="abs arrow" style="left:1060px;top:333px;height:40px"><svg width="14" height="20" viewBox="0 0 14 20"><path d="m3 2 8 8-8 8" fill="none" stroke="#fff" stroke-width="3.5"/></svg></div>
</section>

<section>
  <div class="abs panel" style="left:112px;width:369px"><div class="panel-head">How Medora Works</div></div>
  <div class="abs video">
    <div class="video-frame" role="img" aria-label="Lecture hall with a presenter handing out materials to students"></div>
    <svg class="abs" style="left:149px;top:75px" width="68" height="50" viewBox="0 0 68 50"><rect width="68" height="50" rx="4" fill="#222" opacity=".8"/><path d="M26 12v26l20-13z" fill="#fff"/></svg>
    <div class="video-bar">
      <svg width="12" height="12"><path d="M2 1v10l9-5z" fill="#444"/></svg>
      <svg width="14" height="12"><path d="M1 4h3l4-3v10L4 8H1z" fill="#444"/></svg>
      <span>0:00 / 3:13</span>
      <svg width="92" height="10"><rect y="3" width="92" height="4" rx="2" fill="#aaa"/><rect y="3" width="60" height="4" rx="2" fill="#d04848"/><circle cx="5" cy="5" r="5" fill="#666"/></svg>
      <span style="margin-left:14px">480p</span>
      <svg width="60" height="12"><path d="M4 9l6-6 6 6z" fill="#444"/><path d="M30 5h10v2H30zM34 1h2v10h-2z" fill="#444"/><path d="M50 1h8v8h-8z" fill="none" stroke="#444"/></svg>
    </div>
  </div>

  <div class="abs panel" style="left:492px;width:294px"></div>
  <div class="abs feed">
    <div class="abs" style="left:10px;top:10px;width:30px;height:30px;background:#fff;border-radius:2px"></div>
    <div class="abs" style="left:48px;top:11px;color:#fff;font-size:11px;font-weight:600">Medora Medical Peer Review</div>
    <div class="abs" style="left:48px;top:24px;color:#fff;font-size:17px;font-weight:700">Medora</div>
    <div class="abs feed-body">
      <div class="tw"><span class="who">Medora Medical</span> Why your accountant could be costing you an arm and a leg <a>lnk.example/ab12</a><div class="meta">yesterday · reply · retweet · favorite</div></div>
      <div class="tw"><span class="who">Medora Medical</span>Buyers circle as duty calls <a>news.example.org/property/real-es...</a> via <a>@propertynews</a><div class="meta">2 days ago · reply · retweet · favorite</div></div>
      <div class="tw" style="border:none"><span class="who">Medora Medical</span> Are you eligible for the Payroll Tax Rebate Scheme? Find out here <a>lnk.example/cd34</a><div class="meta">3 days ago · reply · retweet · favorite</div></div>
    </div>
    <div class="abs" style="left:10px;top:235px;color:#fff;font-size:16px;font-weight:700">feed</div>
    <div class="abs" style="left:159px;top:235px;color:#fff;font-size:12px">Join the conversation</div>
  </div>

  <div class="abs social">
    <div class="social-head">
      <div class="abs" role="img" aria-label="Profile picture of a person in a surgical mask" style="left:9px;top:6px;width:38px;height:52px;background:linear-gradient(#cfd6df,#8fb3c9)"></div>
      <div class="abs" style="left:68px;top:9px;font-size:15px;font-weight:600;color:#1d3f7a">Medora <span style="font-size:11px;font-weight:400;color:#333">on Social</span></div>
      <div class="abs" style="left:59px;top:31px;width:47px;height:22px;border:1px solid #9aa8c4;border-radius:3px;background:#f3f5fa;font-size:12px;color:#1d3f7a;text-align:center;line-height:20px">Like</div>
    </div>
    <div class="abs" style="left:8px;top:72px;font-size:12px;color:#333">26,010 people like <b>Brightline Studio</b>.</div>
    <div class="abs" style="left:9px;top:92px;display:grid;grid-template-columns:repeat(5,50px);column-gap:5px;row-gap:4px">
      <div class="friend"><div role="img" aria-label="Profile photo" style="background:#b0683a"></div>Marcus</div>
      <div class="friend"><div role="img" aria-label="Profile photo" style="background:#3bb8c0"></div>Soren</div>
      <div class="friend"><div role="img" aria-label="Profile photo" style="background:#8d7a5e"></div>Kai Nolan</div>
      <div class="friend"><div role="img" aria-label="Profile photo" style="background:#d9a08c"></div>Selma Ines</div>
      <div class="friend"><div role="img" aria-label="Profile photo" style="background:#1b3b3a"></div>Pia Hart</div>
      <div class="friend"><div role="img" aria-label="Profile photo" style="background:#b05a9c"></div>Maren</div>
      <div class="friend"><div role="img" aria-label="Profile photo" style="background:#4a3a30"></div>Kamala Sri</div>
      <div class="friend"><div role="img" aria-label="Profile photo" style="background:#7a7a7a"></div>Kristen</div>
      <div class="friend"><div role="img" aria-label="Profile picture" style="background:#ede4b0"></div>Finn</div>
      <div class="friend"><div role="img" aria-label="Profile photo" style="background:#6a5446"></div>Bryn</div>
    </div>
    <div class="abs" style="left:6px;top:241px;width:267px;border-top:1px solid #ccc"></div>
    <div class="abs" style="left:7px;top:248px;font-size:10px;color:#555;display:flex;gap:5px;align-items:center"><span style="width:11px;height:11px;background:#3b5998;display:block"></span>Social plugin</div>
  </div>
</section>

<footer>
  <div class="abs footer"></div>
  <div class="abs footer-nav"><span>Home</span>|<span>Take The Tour</span>|<span>What YourPeers Say</span>|<span>Subsription Plans</span>|<span>Free Signup</span>|<span>Contact Us</span>|<span>Sitemap</span></div>
  <div class="abs copy">Copyright 2012 medora Limited</div>
</footer>
</body>
</html>
```